Postcard Design

We are a pet resort located near Atlanta's Corbinvale Pruett Airport. I want a postcard that will show dogs playing and the offer will be "New customers receive 50% off boarding" *
* 50% offer applies to standard lodging fees only. Amenities and playtimes not included in this offer. Valid for up to 10 nights of boarding. Blackout dates of July 4th, Thanksgiving week and Christmas week apply. Reservations required.
The backside of the postcard will read, "New daycare customers recieve ONE WEEK of FREE daycare for your dog".*
* offer good for 5 consecutive days of daycare only-not in conjuction with overnight lodging. Good for one pet per family only. Offer not valid on July 4th week, Thanksgiving week or Christmas week.

```html
<!DOCTYPE html>
<html lang="en">
<head>
<meta charset="utf-8">
<title>Daycare Offer Postcard</title>
<link rel="stylesheet" href="https://fonts.googleapis.com/css2?family=Dancing+Script:wght@500&family=Roboto+Condensed:wght@400&family=Arimo&display=swap">
<style>
  :root {
    --brand-red: #cc0010;
    --ink: #111111;
    --paper: #ffffff;
    --mist: #e9e9e9;
    --grass: #4f7a2a;
    --leaf: #b5552a;
  }
  html, body {
    margin: 0;
    padding: 0;
    overflow: hidden;
    background: var(--paper);
  }
  .postcard {
    position: relative;
    width: 1200px;
    height: 923px;
    background: var(--paper);
    overflow: hidden;
  }
  .offer-panel {
    position: absolute;
    left: 0;
    top: 0;
    width: 570px;
    height: 923px;
  }
  .top-band {
    position: absolute;
    left: 0; top: 0;
    width: 570px; height: 18px;
    background: var(--brand-red);
  }
  .hero-photo {
    position: absolute;
    left: 0; top: 18px;
    width: 570px; height: 269px;
    background: linear-gradient(180deg, #20301a 0%, #3e6125 40%, var(--grass) 70%, #6a5a22 100%);
  }
  .headline-block {
    position: absolute;
    left: 0; top: 287px;
    width: 570px; height: 223px;
    background: var(--brand-red);
  }
  .headline {
    margin: 0;
    padding-top: 22px;
    color: var(--paper);
    font-family: "Dancing Script", cursive;
    font-weight: 500;
    font-size: 46px;
    line-height: 61px;
    text-align: center;
  }
  .fine-print-backdrop {
    position: absolute;
    left: 0; top: 510px;
    width: 570px; height: 170px;
    background: linear-gradient(180deg, var(--mist) 0%, var(--paper) 100%);
  }
  .headline-curve {
    position: absolute;
    left: 0; top: 509px;
    width: 570px; height: 40px;
    display: block;
  }
  .terms {
    position: absolute;
    left: 20px; top: 564px;
    width: 545px;
    margin: 0;
    font-family: "Roboto Condensed", sans-serif;
    font-size: 22.5px;
    line-height: 30px;
    color: var(--ink);
  }
  .terms p { margin: 0 0 11px 17px; }
  .terms .first { text-indent: -17px; }
  .postage-box {
    position: absolute;
    left: 975px; top: 75px;
    width: 136px; height: 136px;
    border: 2px solid var(--ink);
    display: flex;
    align-items: center;
    justify-content: center;
    text-align: center;
    font-family: "Arimo", sans-serif;
    font-size: 26px;
    line-height: 32px;
    color: var(--ink);
  }
  .address-line {
    position: absolute;
    left: 695px;
    width: 406px;
    height: 0;
    border-top: 2px solid var(--ink);
  }
</style>
</head>
<body>
<main class="postcard">
  <section class="offer-panel">
    <div class="top-band"></div>
    <div class="hero-photo" role="img" aria-label="Photo of two dogs playing tug with a red toy on green grass scattered with autumn leaves"></div>
    <div class="headline-block">
      <h1 class="headline">New daycare customers<br>recieve ONE WEEK of<br>FREE daycare for your dog*</h1>
    </div>
    <div class="fine-print-backdrop"></div>
    <svg class="headline-curve" viewBox="0 0 570 40" preserveAspectRatio="none" aria-hidden="true">
      <path d="M0 0 H570 V1 H195 C150 1 140 39 100 39 H0 Z" fill="var(--brand-red)"/>
    </svg>
    <div class="terms">
      <p class="first">* Offer good for 5 consecutive days of daycare only-not in conjuction with overnight lodging.</p>
      <p>Good for one pet per family only.</p>
      <p>Offer not valid on July 4th week, Thanksgiving week or Christmas week.</p>
    </div>
  </section>

  <div class="postage-box">Postage<br>Area</div>
  <div class="address-line" style="top:441px"></div>
  <div class="address-line" style="top:512px"></div>
  <div class="address-line" style="top:583px"></div>
  <div class="address-line" style="top:654px"></div>
</main>
</body>
</html>
```